Sprigg Modern Health Food - Takeaway Menu Design

We are looking for a fresh new takeaway menu that signifies our values: Happy, Healthy, Whole. Sprigg is a modern health food restaurant focusing on locally sourced ingredients where everything is made fresh in house. Menu design will display our menu items and food costs. Will provide logo and list of menu items...
Many items, color pallete, and design ideas can be found on our menu section at www.tallsprigg.ca
Target Market(s)
Customers and possible catering targets...
Industry/Entity Type
Restaurant
Requirements
Must have
- Logo, menu items with pricing, 2 or 3 fold takeaway design, address, website, phone number

```html
<!DOCTYPE html>
<html lang="en">
<head>
<meta charset="utf-8">
<title>Sprigg Modern Health Food – Takeaway Menu</title>
<link rel="stylesheet" href="https://fonts.googleapis.com/css2?family=Courier+Prime:ital,wght@0,400;0,700;1,400&family=Dancing+Script:wght@600&display=swap">
<style>
  :root {
    --teal: #3fb0b1;
    --ink: #2f2f2f;
    --ink-soft: #4a4a4a;
    --paper: #ffffff;
    --wash-sand: #d8cfc5;
    --wash-sky: #bfe4e4;
    --frame: #9b8570;
  }
  html, body { margin: 0; padding: 0; overflow: hidden; background: var(--paper); }
  .menu {
    position: relative; width: 1200px; height: 777px; overflow: hidden;
    background: var(--paper); color: var(--ink);
    font-family: "Courier Prime", "Courier New", monospace;
  }
  .washes { position: absolute; inset: 0; }
  .panel-frame {
    position: absolute; top: 6px; bottom: 6px;
    border: 1.5px dashed var(--frame);
  }
  .panel-frame--left { left: 6px; width: 584px; }
  .panel-frame--right { left: 605px; width: 588px; }

  .section-title {
    position: absolute; margin: 0;
    font-family: "Dancing Script", cursive; font-weight: 600;
    color: var(--teal); line-height: 1; white-space: nowrap;
  }
  .section-note {
    position: absolute; margin: 0; font-size: 9.6px; line-height: 10.5px;
    color: var(--ink-soft); white-space: nowrap;
  }
  .section-note--ruled { border-bottom: 1px solid #9a9a9a; padding-bottom: 1px; }

  .item { position: absolute; }
  .item-head {
    display: flex; align-items: baseline; font-size: 11px; line-height: 12px;
    color: var(--ink); white-space: nowrap;
  }
  .item-leader {
    flex: 1; margin: 0 1px; border-bottom: 1.5px dotted var(--ink); transform: translateY(-2px);
  }
  .item-desc {
    margin: 1px 0 0; font-size: 7.6px; line-height: 8.4px; color: var(--ink-soft);
  }
  .bennie-note {
    position: absolute; margin: 0; font-size: 8.4px; line-height: 9px;
    font-style: italic; text-align: center; color: var(--ink);
  }
  .feature {
    position: absolute; text-align: center; font-size: 10.5px; line-height: 12px; color: var(--ink);
  }
  .size-tag { position: absolute; margin: 0; font-size: 14px; line-height: 14px; color: var(--ink); }
  .contact {
    position: absolute; left: 620px; top: 752px; width: 560px; margin: 0;
    display: flex; align-items: center; gap: 6px;
    font-size: 8px; line-height: 9px; color: var(--ink-soft); white-space: nowrap;
  }
  .contact-mark { width: 7px; height: 7px; border-radius: 50%; background: var(--teal); }
  .contact-name { color: var(--teal); }
</style>
</head>
<body>
<main class="menu">

  <svg class="washes" width="1200" height="777" viewBox="0 0 1200 777" role="img"
       aria-label="Soft watercolour washes in sand and sky blue with hand-sketched vegetables">
    <defs>
      <filter id="soft" x="-20%" y="-20%" width="140%" height="140%"><feGaussianBlur stdDeviation="14"/></filter>
    </defs>
    <g filter="url(#soft)" opacity="0.9">
      <path fill="var(--wash-sand)" d="M0 0 H560 C540 80 520 150 470 180 C420 230 330 240 230 250 C150 262 60 270 0 260 Z"/>
      <path fill="var(--wash-sand)" d="M860 0 H1200 V230 C1130 250 1030 240 960 210 C900 170 870 100 860 0 Z"/>
      <path fill="var(--wash-sky)" d="M0 440 C120 410 250 420 380 400 C480 390 560 410 590 430 V777 H0 Z"/>
      <path fill="var(--wash-sky)" d="M360 430 C450 390 560 360 640 380 C760 350 880 360 960 420 C1010 470 990 560 940 620 C880 700 760 777 700 777 H380 C400 650 380 540 360 430 Z"/>
    </g>
  </svg>

  <div class="panel-frame panel-frame--left"></div>
  <div class="panel-frame panel-frame--right"></div>

  <!-- Rice Bowls -->
  <h2 class="section-title" style="left:246px; top:30px; font-size:38px;">Rice Bowls</h2>
  <p class="section-note" style="left:246px; top:73px;">For the following menu items:</p>
  <p class="section-note section-note--ruled" style="left:246px; top:83px;">add Chicken $3.00 / add Tofu $2.50</p>

  <div class="item" style="left:82px; top:111px; width:212px;">
    <div class="item-head"><span>Coconut Chili Bowl</span><span class="item-leader"></span><span>$12.25</span></div>
    <p class="item-desc">Brown Rice, kidney beans, chickpeas, corn, red onion, coconut milk, greens, grated carrot, sprigg chili spice blend</p>
  </div>
  <div class="item" style="left:82px; top:155px; width:212px;">
    <div class="item-head"><span>Falafel Bowl</span><span class="item-leader"></span><span>$12.25</span></div>
    <p class="item-desc">Brown rice, gf falafels, greens, hummus, banana peppers, red onion, cucumber, house cilantro lime sc</p>
  </div>
  <div class="item" style="left:82px; top:200px; width:212px;">
    <div class="item-head"><span>Urban Bowl</span><span class="item-leader"></span><span>$12.25</span></div>
    <p class="item-desc">Brown rice, greens, grated carrot, beets, red cabbage, tamari mushrooms, hemp hearts, sprouts, house tamari sc</p>
  </div>
  <div class="item" style="left:322px; top:111px; width:212px;">
    <div class="item-head"><span>Miso BBQ Bowl</span><span class="item-leader"></span><span>$12.25</span></div>
    <p class="item-desc">Brown rice, greens, bbq tempeh, sweet potato, grated carrot, beet, pickled onion, pumpkin seeds, house bbq miso sc</p>
  </div>
  <div class="item" style="left:322px; top:155px; width:212px;">
    <div class="item-head"><span>Red Curry Bowl</span><span class="item-leader"></span><span>$12.25</span></div>
    <p class="item-desc">Brown rice, greens, avocado, black beans, carrot, cucumber, salsa, yogurt, house red curry sc</p>
  </div>

  <!-- Grilled Sandwiches -->
  <h2 class="section-title" style="left:292px; top:236px; font-size:37px;">Grilled Sandwiches</h2>
  <p class="section-note section-note--ruled" style="left:399px; top:281px; font-size:10.5px;">Sprouted grain or Gluten free</p>

  <div class="item" style="left:52px; top:303px; width:245px;">
    <div class="item-head"><span>Grilled Breakfast Sandwich</span><span class="item-leader"></span><span>$9.95</span></div>
    <p class="item-desc">Fried egg on alder micro sour bread, with smoked gouda, tomato, and spinach, served with a side of russian sauce. (Add montreal smoked beef or turkey bacon $3.00)</p>
  </div>
  <div class="item" style="left:52px; top:350px; width:245px;">
    <div class="item-head"><span>Spicy Chicken</span><span class="item-leader"></span><span>$9.95</span></div>
    <p class="item-desc">Chicken breast, smoked gouda, spinach, tomato, banana peppers, chipotle mayo</p>
  </div>
  <div class="item" style="left:52px; top:387px; width:245px;">
    <div class="item-head"><span>Sprigg Reuben</span><span class="item-leader"></span><span>$9.95</span></div>
    <p class="item-desc">Montreal smoked beef, saurkraut, smoked gouda, dijon mustard, house russian sc</p>
  </div>
  <div class="item" style="left:323px; top:303px; width:231px;">
    <div class="item-head"><span>Carrot Tempeh</span><span class="item-leader"></span><span>$9.95</span></div>
    <p class="item-desc">Smoked bbq temph, grated carrot, greens, tomato, avocado, red onion, dijon mustard, bbq miso sauce</p>
  </div>
  <div class="item" style="left:323px; top:341px; width:231px;">
    <div class="item-head"><span>Black Bean Torta</span><span class="item-leader"></span><span>$9.95</span></div>
    <p class="item-desc">Creamy black beans, greens, tomatoes, pickled red onion, avocado, chipotle mayo</p>
  </div>
  <div class="item" style="left:323px; top:378px; width:231px;">
    <div class="item-head"><span>Lentil Veggie Burger</span><span class="item-leader"></span><span>$9.95</span></div>
    <p class="item-desc">Lentil &amp; sweet potato pattie, tomato avocado, soy cheese, greens, dijon mustard, served on a spelt bun, house chipotle mayo</p>
  </div>

  <!-- Grilled Wraps -->
  <h2 class="section-title" style="left:78px; top:455px; font-size:36px;">Grilled Wraps</h2>
  <p class="section-note section-note--ruled" style="left:94px; top:500px; font-size:10.5px;">Sprouted grain or Gluten free</p>

  <div class="item" style="left:65px; top:525px; width:229px;">
    <div class="item-head"><span>Breakfast Burrito</span><span class="item-leader"></span><span>$10.95</span></div>
    <p class="item-desc">Your choice of egg or tofu scramble, avocado, tomato, gouda, salsa, spinach, served with a side of salsa</p>
  </div>
  <div class="item" style="left:65px; top:561px; width:229px;">
    <div class="item-head"><span>Falafel</span><span class="item-leader"></span><span>$10.95</span></div>
    <p class="item-desc">Brown rice, baked falafels, hummus, avocado, red cabbage, pickled onion, spinach, house cilantro lime sc</p>
  </div>
  <div class="item" style="left:65px; top:607px; width:229px;">
    <div class="item-head"><span>Veggie Burrito</span><span class="item-leader"></span><span>$10.95</span></div>
    <p class="item-desc">Brown rice, black beans, corn, sweet potato, red cabbage, house coconut chipotle mayo</p>
  </div>
  <div class="item" style="left:65px; top:644px; width:229px;">
    <div class="item-head"><span>BBQ Chicken</span><span class="item-leader"></span><span>$10.95</span></div>
    <p class="item-desc">Chicken, brown rice, organic greens, red cabbage, avocado, bbq miso sauce</p>
  </div>
  <div class="item" style="left:65px; top:681px; width:229px;">
    <div class="item-head"><span>Urban Wrap</span><span class="item-leader"></span><span>$10.95</span></div>
    <p class="item-desc">Brown rice, organic greens, grated carrots, beets, purple cabbage, tamari</p>
  </div>

  <!-- Daily Salad & Soup -->
  <h2 class="section-title" style="left:350px; top:462px; width:180px; text-align:center; font-size:38px;">Daily Salad</h2>
  <div class="feature" style="left:330px; top:513px; width:220px;">Your choice of salads,<br>$4.95 side $3.75</div>
  <h2 class="section-title" style="left:350px; top:558px; width:180px; text-align:center; font-size:38px;">Daily Soup</h2>
  <div class="feature" style="left:320px; top:614px; width:240px;">Farm to Table, fresh and inspired<br>$6.00 side $4.00</div>

  <!-- Sprigg Breakfast -->
  <h2 class="section-title" style="left:632px; top:62px; font-size:36px;">Sprigg Breakfast</h2>
  <p class="section-note" style="left:633px; top:104px;">Serving local farm fresh eggs</p>
  <p class="section-note section-note--ruled" style="left:633px; top:114px;">Served until 12pm weekdays &amp; 2pm weekends</p>

  <div class="item" style="left:631px; top:139px; width:256px;">
    <div class="item-head"><span>Breakfast Bowl</span><span class="item-leader"></span><span>$12.00</span></div>
    <p class="item-desc">Roasted roots topped with two poached eggs, black beans, rice, avocado, banana peppers spinach and salsa topped with our house made cilantro lime dressing</p>
  </div>
  <div class="item" style="left:631px; top:191px; width:256px;">
    <div class="item-head"><span>Pancakes</span><span class="item-leader"></span><span>$8.95</span></div>
    <p class="item-desc">3 buckwheat pancakes, turkey bacon, or montreal smoked beef w/ maple syrup, or side of fruit or roots</p>
  </div>
  <div class="item" style="left:631px; top:233px; width:256px;">
    <div class="item-head"><span>Grilled Breakfast Burrito</span><span class="item-leader"></span><span>$10.95</span></div>
    <p class="item-desc">Your choice of egg or tofu scramble, avocado, tomato, gouda, salsa, spinach, served with a side of salsa</p>
  </div>
  <div class="item" style="left:631px; top:269px; width:256px;">
    <div class="item-head"><span>Two Eggs (your way)</span><span class="item-leader"></span><span>$8.95</span></div>
    <p class="item-desc">Eggs, toast, turkey bacon or corned beef and roasted roots</p>
  </div>
  <div class="item" style="left:631px; top:303px; width:256px;">
    <div class="item-head"><span>Side Toast</span><span class="item-leader"></span><span>$3.95</span></div>
    <p class="item-desc">Two pieces alder micro sour or gluten free bread w/ peanut butter, almond butter or jam</p>
  </div>
  <div class="item" style="left:631px; top:339px; width:256px;">
    <div class="item-head"><span>Side of Pancakes</span><span class="item-leader"></span><span>$5.50</span></div>
    <p class="item-desc">Two buckwheat pancakes w/ maple syrup</p>
  </div>

  <!-- Eggs Bennie -->
  <div class="item" style="left:914px; top:241px; width:255px;">
    <div class="item-head"><span>Eggs Bennie</span></div>
    <p class="item-desc">English muffin (available gluten free) two poached eggs, roasted roots and hollandaise. See below:</p>
  </div>
  <p class="bennie-note" style="left:914px; top:279px; width:255px;">Or have your Bennie in a Bowl served<br>on Roasted Sprigg!!</p>
  <div class="item" style="left:914px; top:302px; width:255px;">
    <div class="item-head"><span>Very Veggie Bennie</span><span class="item-leader"></span><span>$11.95</span></div>
    <p class="item-desc">Spinach, tomato, avocado</p>
  </div>
  <div class="item" style="left:914px; top:329px; width:255px;">
    <div class="item-head"><span>Montreal Smoked Beef Bennie</span><span class="item-leader"></span><span>$12.25</span></div>
    <p class="item-desc">Montreal smoked beef, spinach, tomato</p>
  </div>
  <div class="item" style="left:914px; top:357px; width:255px;">
    <div class="item-head"><span>Smoked Salmon Bennie</span><span class="item-leader"></span><span>$13.95</span></div>
    <p class="item-desc">Smoked salmon, spinach, capers</p>
  </div>

  <!-- Smoothies -->
  <h2 class="section-title" style="left:992px; top:420px; font-size:37px;">Smoothies</h2>
  <p class="size-tag" style="left:1090px; top:456px;">16oz</p>

  <div class="item" style="left:910px; top:489px; width:231px;">
    <div class="item-head"><span>Mylkshake</span><span class="item-leader"></span><span>$6.75</span></div>
    <p class="item-desc">Almond milk, avocado, banana, vanilla, matcha, dates</p>
  </div>
  <div class="item" style="left:910px; top:525px; width:231px;">
    <div class="item-head"><span>Breakfast Smoothie</span><span class="item-leader"></span><span>$6.75</span></div>
    <p class="item-desc">Mixed berries, banana, spinach, almond milk &amp; coconut water</p>
  </div>
  <div class="item" style="left:910px; top:561px; width:231px;">
    <div class="item-head"><span>Green Protein</span><span class="item-leader"></span><span>$7.25</span></div>
    <p class="item-desc">Kale, spinach, lemon, almond meal, avocado, spirulina, honey, vanilla, banana, dates, almond milk</p>
  </div>
  <div class="item" style="left:910px; top:599px; width:231px;">
    <div class="item-head"><span>Frozen Hot Chocolate</span><span class="item-leader"></span><span>$6.75</span></div>
    <p class="item-desc">Cacao, macca, dates, cinnamon, avocado, honey, vanilla, coconut milk</p>
  </div>
  <div class="item" style="left:910px; top:636px; width:231px;">
    <div class="item-head"><span>Brain Booster</span><span class="item-leader"></span><span>$6.75</span></div>
    <p class="item-desc">Carrot juice, blueberries, beet, apple, ginger, lemon, almond milk</p>
  </div>
  <div class="item" style="left:910px; top:673px; width:231px;">
    <div class="item-head"><span>Blueberry Matcha</span><span class="item-leader"></span><span>$6.75</span></div>
    <p class="item-desc">Blueberries, banana, dates, matcha, cinnamon, almond milk</p>
  </div>

  <!-- Brand & contact -->
  <footer class="contact">
    <span class="contact-mark"></span>
    <span class="contact-name">Sprigg Modern Health Food</span>
    <span>412 Front Street, Alder BC</span>
    <span>250-555-0142</span>
    <span>www.tallsprigg.ca</span>
  </footer>

</main>
</body>
</html>
```